Looking to update current business card

We have a two sided card currently that needs a fresher, newer look. I like the fact it has two sides with a list of products/services we offer on the back side but the overall front look is lackluster. Our logo will stay the same.. I just want someone to bring some new life into the business card.

I like cards that have rounded corners but not sure if there's enough room?

Attached is our current biz card design and logo.

Target Market(s)

business customers

Industry/Entity Type

Business

Contact Information for Business Card

see above

```html
<!DOCTYPE html>
<html lang="en">
<head>
<meta charset="utf-8">
<title>Corvid Secure – Business Card, Front and Back</title>
<link rel="stylesheet" href="https://fonts.googleapis.com/css2?family=Exo+2:wght@400;500;600;700&display=swap">
<style>
  :root {
    --stage: #e6e7e9;
    --card-white: #ffffff;
    --card-grey: #dfe0e2;
    --brand-blue: #3d6190;
    --brand-orange: #f28c55;
    --ink-white: #ffffff;
  }
  html, body {
    margin: 0;
    padding: 0;
    width: 1200px;
    height: 899px;
    overflow: hidden;
    background: var(--stage);
    font-family: "Exo 2", sans-serif;
  }
  .canvas {
    position: relative;
    width: 1200px;
    height: 899px;
  }
  .card {
    position: absolute;
    left: 240px;
    width: 720px;
    height: 411px;
    border-radius: 32px;
    overflow: hidden;
    box-shadow: 0 10px 28px rgba(0,0,0,0.16);
  }
  .card-front { top: 24px; }
  .card-back  { top: 464px; background: linear-gradient(160deg, var(--card-white) 0%, var(--card-grey) 100%); }
  .card-art {
    position: absolute;
    inset: 0;
    width: 100%;
    height: 100%;
  }
  .brand {
    position: absolute;
    display: flex;
    align-items: center;
    gap: 10px;
  }
  .card-front .brand {
    left: 46px;
    top: 64px;
  }
  .card-back .brand {
    left: 0;
    right: 0;
    top: 0;
    bottom: 0;
    justify-content: center;
  }
  .brand-name {
    font-size: 33px;
    font-weight: 700;
    color: var(--brand-blue);
    letter-spacing: 1px;
    line-height: 1;
  }
  .card-back .brand-name { font-size: 38px; }
  .brand-dot {
    width: 16px;
    height: 16px;
    border-radius: 50%;
    background: var(--brand-orange);
  }
  .card-back .brand-dot { width: 18px; height: 18px; }
  .person {
    position: absolute;
    right: 44px;
    top: 60px;
    text-align: right;
    color: var(--brand-orange);
  }
  .person-name {
    font-size: 23px;
    font-weight: 600;
    letter-spacing: 1.5px;
    margin: 0;
    line-height: 1.2;
  }
  .person-title {
    font-size: 17px;
    font-weight: 500;
    margin: 3px 0 0;
  }
  .contact {
    position: absolute;
    right: 34px;
    top: 216px;
    margin: 0;
    padding: 0;
    list-style: none;
    color: var(--ink-white);
    font-size: 14px;
    font-weight: 500;
    text-align: right;
    line-height: 22px;
  }
  .contact li {
    display: flex;
    justify-content: flex-end;
    align-items: center;
    gap: 8px;
  }
  .contact .address {
    display: block;
    padding-right: 22px;
    line-height: 20px;
    margin-bottom: 6px;
  }
  .contact svg {
    width: 13px;
    height: 13px;
    flex: none;
  }
</style>
</head>
<body>
<main class="canvas">
  <section class="card card-front" aria-label="Corvid Secure business card, front">
    <svg class="card-art" viewBox="0 0 1000 571" preserveAspectRatio="none" aria-hidden="true">
      <defs>
        <linearGradient id="paper-front" x1="0" y1="0" x2="0.6" y2="1">
          <stop offset="0" stop-color="#ffffff"/>
          <stop offset="1" stop-color="#dfe0e2"/>
        </linearGradient>
      </defs>
      <rect width="1000" height="571" fill="url(#paper-front)"/>
      <path d="M0,292 C200,238 360,318 570,262 C760,212 870,196 1000,200 L1000,571 L0,571 Z" fill="var(--brand-orange)"/>
      <path d="M0,322 C200,268 365,348 585,292 C765,246 872,232 1000,236 L1000,571 L0,571 Z" fill="#ffffff"/>
      <path d="M0,334 C200,282 370,362 590,306 C770,260 875,248 1000,252 L1000,571 L0,571 Z" fill="var(--brand-blue)"/>
    </svg>

    <div class="brand">
      <span class="brand-name">CORVID SECURE</span>
      <span class="brand-dot"></span>
    </div>

    <div class="person">
      <p class="person-name">MARCUS HOLLOWAY</p>
      <p class="person-title">Managing Director</p>
    </div>

    <ul class="contact">
      <li class="address">214, 9th Floor, Harbor Point<br>Road QLN</li>
      <li>020 555 0147
        <svg viewBox="0 0 24 24"><path fill="#fff" d="M6.6 10.8a15.1 15.1 0 0 0 6.6 6.6l2.2-2.2c.3-.3.7-.4 1-.2 1.1.4 2.3.6 3.6.6.6 0 1 .4 1 1V20c0 .6-.4 1-1 1A17 17 0 0 1 3 4c0-.6.4-1 1-1h3.5c.6 0 1 .4 1 1 0 1.3.2 2.5.6 3.6.1.3 0 .7-.2 1z"/></svg>
      </li>
      <li>020 555 0148
        <svg viewBox="0 0 24 24"><rect x="6" y="2" width="12" height="20" rx="2" fill="none" stroke="#fff" stroke-width="2"/><circle cx="12" cy="18" r="1.2" fill="#fff"/></svg>
      </li>
      <li>020 555 0149
        <svg viewBox="0 0 24 24"><rect x="3" y="9" width="18" height="11" rx="1.5" fill="#fff"/><rect x="7" y="3" width="10" height="6" fill="none" stroke="#fff" stroke-width="2"/></svg>
      </li>
      <li>hello@corvidsecure.test
        <svg viewBox="0 0 24 24"><rect x="3" y="5" width="18" height="14" rx="1.5" fill="#fff"/><path d="M3 6l9 7 9-7" fill="none" stroke="var(--brand-blue)" stroke-width="1.8"/></svg>
      </li>
      <li>www.corvidsecure.test
        <svg viewBox="0 0 24 24"><circle cx="12" cy="12" r="9" fill="none" stroke="#fff" stroke-width="2"/><ellipse cx="12" cy="12" rx="4" ry="9" fill="none" stroke="#fff" stroke-width="1.6"/><path d="M3 12h18" stroke="#fff" stroke-width="1.6"/></svg>
      </li>
    </ul>
  </section>

  <section class="card card-back" aria-label="Corvid Secure business card, back">
    <div class="brand">
      <span class="brand-name">CORVID SECURE</span>
      <span class="brand-dot"></span>
    </div>
  </section>
</main>
</body>
</html>
```